Introduction:
We are an Australia-based Cyber Security Penetration testing company seeking a website redesign to showcase our services, expertise, and experience. Our target audience includes businesses and organizations of all sizes who are seeking to secure their IT infrastructure against cyber threats. The purpose of the website redesign is to increase our online presence, generate leads, and establish our company as a trusted authority in the industry.
Objectives:
Create a professional and modern website that is easy to navigate and user-friendly.
Provide information about our company, services, and expertise.
Clearly display table of our 3 services: Bug Bounty as a Service, Penetration Testing and Code Review.
Generate leads through online contact forms and calls-to-action.
Optimize the website for search engines to increase visibility and traffic.
Website similar to: https://www.velmoro.com.au/.
Target Audience:
Our target audience includes businesses and organizations of all sizes that require cybersecurity penetration testing services. These include:
Small and medium-sized enterprises (SMEs)
Australian Government agencies
Design Requirements:
Clean, modern, and professional design.
Use of colors that convey trust, reliability, and expertise (such as orange and grey).
Calls-to-action that encourage visitors to contact us or request a quote.
Integration with social media channels to increase engagement and brand awareness.
A blog section to showcase our thought leadership and expertise.
A news section to share updates about our company and the industry.
Content Requirements:
Home page that introduces our company and services and highlights our expertise.
About Us page that provides information about our company, team, and values.
Services page that lists our services and explains the benefits of each.
Case Studies page that showcases our previous work and success stories.
Contact Us page that includes a contact form, phone number, and email address.
Blog section with articles related to the cybersecurity industry and our services.
News section with updates about our company and the industry.
Look and feel
Each slider illustrates characteristics of the customer's brand and the style your logo design should communicate.

```html
<!DOCTYPE html>
<html lang="en">
<head>
<meta charset="utf-8">
<title>Emberstrata – Cyber Security Penetration Testing</title>
<link rel="stylesheet" href="https://fonts.googleapis.com/css2?family=Poppins:wght@400;500;600;700;800&family=Lato:wght@400;700&display=swap">
<style>
:root{
  --orange:#ef6b2b;
  --amber:#f2a43f;
  --ink:#3b3b3b;
  --body:#555;
  --dark:#2b2b2b;
  --hero-a:#15171c;
  --hero-b:#1d3a46;
  --card:#fdf2ea;
  --line:#9a9a9a;
  --white:#fff;
}
*{margin:0;padding:0;box-sizing:border-box}
html,body{width:1200px;height:3303px;overflow:hidden}
body{position:relative;font-family:"Poppins",sans-serif;color:var(--ink);background:var(--white)}
.abs{position:absolute}
.btn{position:absolute;display:flex;align-items:center;justify-content:center;background:var(--orange);color:var(--white);font-weight:600;border-radius:30px;font-size:19px}
.accent{color:var(--orange)}

/* hero */
.hero{left:0;top:0;width:1200px;height:737px;background:linear-gradient(100deg,var(--hero-a) 0%,#2a2a30 35%,#1a2c36 65%,var(--hero-b) 100%)}
.hero-visual{left:640px;top:110px;width:520px;height:560px;border-radius:50%;background:radial-gradient(circle,#2f6d80 0%,#1b3d4a 45%,transparent 72%);opacity:.9}
.brand{left:74px;top:62px;display:flex;align-items:center;gap:12px;font-size:38px;font-weight:600;color:var(--orange)}
.brand-dot{width:26px;height:26px;border-radius:50%;background:var(--orange);flex:none}
.nav{left:382px;top:72px;display:flex;gap:40px;font-size:17px;font-weight:600;color:var(--white)}
.nav .current{color:var(--orange)}
.hero-title{left:72px;top:272px;font-size:76px;font-weight:700;color:var(--white);letter-spacing:1px}
.hero-sub{left:76px;top:372px;width:560px;font-size:36px;font-weight:600;line-height:40px;color:var(--white)}
.hero .btn{left:76px;top:526px;width:177px;height:54px}

/* section headings */
.h2{font-size:48px;font-weight:700;color:var(--ink)}

/* about */
.about-visual{left:74px;top:817px;width:486px;height:352px;border-radius:190px 190px 130px 130px;background:linear-gradient(135deg,#4a4a4a,#2e6c93 50%,#1c3c5a)}
.about-title{left:617px;top:818px;line-height:52px}
.about-text{left:615px;top:943px;width:505px;font-size:17px;line-height:33px;color:var(--body)}
.about .btn{left:615px;top:1101px;width:179px;height:54px}

/* services */
.centre{left:0;width:1200px;text-align:center}
.services-title{top:1276px}
.services-intro{top:1352px;left:70px;width:1060px;font-size:17.5px;line-height:33px;color:var(--body);text-align:center}
.svc{top:1470px;width:329px;height:291px;background:var(--card);border-radius:40px;text-align:center}
.svc svg{position:absolute;left:118px;top:34px}
.svc h3{position:absolute;top:140px;width:100%;font-size:26px;font-weight:600;color:var(--ink)}
.svc p{position:absolute;top:182px;left:28px;width:273px;font-size:17.5px;line-height:28px;color:var(--body)}

/* expertise */
.exp-title{top:1872px}
.exp{top:2026px;width:243px;height:298px;background:var(--amber);border-radius:40px 40px 0 0;text-align:center;color:var(--white)}
.exp .badge{position:absolute;left:69px;top:-52px;width:104px;height:104px;border-radius:50%;background:var(--orange);border:5px solid var(--white);display:flex;align-items:center;justify-content:center}
.exp h3{position:absolute;top:76px;width:100%;font-size:23px;font-weight:700}
.exp p{position:absolute;top:116px;left:18px;width:207px;font-size:15px;line-height:26px}
.exp .more{position:absolute;left:50px;top:220px;width:143px;height:44px;border:2px solid var(--white);border-radius:24px;display:flex;align-items:center;justify-content:center;font-size:15px;font-weight:600}

/* contact */
.contact-bg{left:0;top:2400px;width:1200px;height:574px;background:linear-gradient(180deg,#fff 0%,#fff 55%,#f2f2f3 100%)}
.contact-brand{left:74px;top:2640px;width:420px;display:flex;align-items:center;gap:14px;font-size:54px;font-weight:600;color:var(--orange);white-space:nowrap}
.contact-brand .brand-dot{width:40px;height:40px}
.contact-title{left:526px;top:2440px}
.field{position:absolute;border:1.5px solid var(--line);border-radius:30px;background:var(--white);font-family:"Lato",sans-serif;font-size:16px;color:#444;padding:0 22px;display:flex;align-items:center}
.field.area{border-radius:14px;align-items:flex-start;padding-top:20px}
.contact .btn{left:526px;top:2831px;width:288px;height:56px}

/* footer */
.footer{left:0;top:2974px;width:1200px;height:329px;background:var(--dark);color:var(--white)}
.footer h4{position:absolute;top:60px;font-size:19px;font-weight:600}
.links{position:absolute;top:94px;font-size:15px;line-height:34px}
.info{position:absolute;left:620px;font-size:15px;line-height:27px}
.info-icon{position:absolute;left:587px}
.social{position:absolute;top:98px;left:885px;display:flex;gap:22px}
.social span{width:26px;height:26px;border-radius:50%;border:2.5px solid var(--white)}
.rule{position:absolute;left:0;top:267px;width:1200px;height:1px;background:#444}
.copy{position:absolute;top:286px;width:1200px;text-align:center;font-family:"Lato",sans-serif;font-size:14px}
</style>
</head>
<body>

<section class="hero abs">
  <div class="hero-visual abs" role="img" aria-label="Person touching a glowing digital interface reading penetration test"></div>
  <div class="brand abs"><span class="brand-dot"></span>Emberstrata</div>
  <nav class="nav abs">
    <span class="current">Home</span><span>About Us</span><span>Services</span><span>Case Studies</span><span>Blog</span><span>News</span><span>Contact Us</span>
  </nav>
  <h1 class="hero-title abs">Emberstrata</h1>
  <p class="hero-sub abs">We are an Australia-based Cyber Security Penetration Testing company</p>
  <a class="btn">Contact Us</a>
</section>

<section class="about">
  <div class="about-visual abs" role="img" aria-label="Two security analysts reviewing a tablet in a server room, framed in a cloud shape"></div>
  <h2 class="h2 about-title abs">About<br><span class="accent">Emberstrata</span></h2>
  <p class="about-text abs">Nemo enim ipsam voluptatem quia voluptas sit aspernatur aut odit aut fugit, sed quia consequuntur magni dolores eos qui ratione voluptatem sequi nesciunt quasi architecto beatae vitae dicta sunt.</p>
  <a class="btn">Read More</a>
</section>

<section class="services">
  <h2 class="h2 centre abs services-title">Our <span class="accent">Services</span></h2>
  <p class="services-intro abs">Nemo enim ipsam voluptatem quia voluptas sit&nbsp; aspernatur aut odit aut fugit, sed quia consequuntur magni dolores eos qui ratione voluptatem sequi nesciunt quasi architecto beatae vitae dicta sunt.</p>

  <div class="svc abs" style="left:74px">
    <svg width="94" height="90" viewBox="0 0 94 90" fill="none" stroke="#ef6b2b" stroke-width="3">
      <ellipse cx="34" cy="46" rx="20" ry="26"/><circle cx="34" cy="16" r="9"/>
      <path d="M14 36H2M14 52H2M54 36h8M34 20v52M22 8l-6-6M46 8l6-6"/>
      <circle cx="70" cy="56" r="20"/><path d="M76 48h-9a4 4 0 0 0 0 8h6a4 4 0 0 1 0 8h-10M70 44v24"/>
    </svg>
    <h3>Bug Bounty</h3>
    <p>Nemo enim ipsam voluptatem quia voluptas sit aspernatur aut odit aut fugit.</p>
  </div>

  <div class="svc abs" style="left:437px">
    <svg width="94" height="90" viewBox="0 0 94 90" fill="#ef6b2b">
      <rect x="2" y="38" width="88" height="50" rx="2"/>
      <path d="M2 55h88M2 71h88M24 38v17M50 38v17M70 38v17M14 55v16M38 55v16M62 55v16M80 55v16M24 71v17M50 71v17M70 71v17" stroke="#fff" stroke-width="3"/>
      <path d="M46 2l20 7v14c0 12-9 19-20 22-11-3-20-10-20-22V9z"/>
      <circle cx="46" cy="20" r="4" fill="#fff"/><rect x="44" y="22" width="4" height="8" fill="#fff"/>
    </svg>
    <h3>Penetration Testing</h3>
    <p>Nemo enim ipsam voluptatem quia voluptas sit aspernatur aut odit aut fugit.</p>
  </div>

  <div class="svc abs" style="left:799px">
    <svg width="94" height="90" viewBox="0 0 94 90" fill="none" stroke="#ef6b2b" stroke-width="3">
      <circle cx="40" cy="40" r="36"/><circle cx="40" cy="40" r="27"/>
      <path d="M28 34l-7 6 7 6M52 34l7 6-7 6M44 30l-8 20M66 66l20 20"/>
    </svg>
    <h3>Code Review</h3>
    <p>Nemo enim ipsam voluptatem quia voluptas sit aspernatur aut odit aut fugit.</p>
  </div>
</section>

<section class="expertise">
  <h2 class="h2 centre abs exp-title">Our <span class="accent">Expertise</span></h2>

  <div class="exp abs" style="left:74px">
    <div class="badge"><svg width="48" height="44" viewBox="0 0 48 44" fill="none" stroke="#fff" stroke-width="2.5"><rect x="2" y="4" width="44" height="28" rx="2"/><path d="M24 34v6M14 42h20M24 10l8 3v6c0 5-4 8-8 9-4-1-8-4-8-9v-6z"/></svg></div>
    <h3>Excepteur Sint</h3>
    <p>Nemo enim ipsam voluptatem quia voluptas sit&nbsp; aspernatur aut.</p>
    <span class="more">Read More</span>
  </div>

  <div class="exp abs" style="left:344px">
    <div class="badge"><svg width="48" height="44" viewBox="0 0 48 44" fill="none" stroke="#fff" stroke-width="2.5"><rect x="6" y="12" width="26" height="24" rx="2"/><path d="M2 40h44M12 20l6 6M18 20l-6 6M22 22h6"/><circle cx="38" cy="12" r="6"/></svg></div>
    <h3>Excepteur Sint</h3>
    <p>Nemo enim ipsam voluptatem quia voluptas sit&nbsp; aspernatur aut.</p>
    <span class="more">Read More</span>
  </div>

  <div class="exp abs" style="left:615px">
    <div class="badge"><svg width="48" height="44" viewBox="0 0 48 44" fill="none" stroke="#fff" stroke-width="2.5"><rect x="8" y="22" width="32" height="18" rx="2"/><path d="M2 42h44M14 20a10 10 0 0 1 20 0"/><circle cx="24" cy="31" r="3"/></svg></div>
    <h3>Excepteur Sint</h3>
    <p>Nemo enim ipsam voluptatem quia voluptas sit&nbsp; aspernatur aut.</p>
    <span class="more">Read More</span>
  </div>

  <div class="exp abs" style="left:885px">
    <div class="badge"><svg width="48" height="44" viewBox="0 0 48 44" fill="none" stroke="#fff" stroke-width="2.5"><circle cx="22" cy="22" r="18"/><path d="M4 22h36M22 4v36M10 10c8 6 16 6 24 0M10 34c8-6 16-6 24 0"/><circle cx="36" cy="32" r="8" fill="#ef6b2b"/><path d="M32 32l3 3 5-5"/></svg></div>
    <h3>Excepteur Sint</h3>
    <p>Nemo enim ipsam voluptatem quia voluptas sit&nbsp; aspernatur aut.</p>
    <span class="more">Read More</span>
  </div>
</section>

<section class="contact">
  <div class="contact-bg abs"></div>
  <div class="contact-brand abs"><span class="brand-dot"></span>Emberstrata</div>
  <h2 class="h2 contact-title abs">Quick <span class="accent">Contact</span></h2>
  <div class="field" style="left:526px;top:2541px;width:288px;height:56px">Name</div>
  <div class="field" style="left:836px;top:2541px;width:290px;height:56px">Email Address</div>
  <div class="field" style="left:526px;top:2613px;width:288px;height:56px">Phone No</div>
  <div class="field" style="left:836px;top:2613px;width:290px;height:56px">Subject</div>
  <div class="field area" style="left:526px;top:2687px;width:600px;height:128px">Message</div>
  <a class="btn">Submit</a>
</section>

<footer class="footer abs">
  <h4 style="left:74px">Quick Links</h4>
  <div class="links" style="left:74px">Home<br>About Us<br>Services<br>Case Studies</div>
  <div class="links" style="left:226px">Blog<br>News<br>Contact Us</div>

  <h4 style="left:376px">Services</h4>
  <div class="links" style="left:376px">Bug Bounty<br>Penetration Testing<br>Code Review</div>

  <h4 style="left:587px">Contact Info</h4>
  <svg class="info-icon" style="top:98px" width="16" height="14" viewBox="0 0 16 14" fill="#f2a43f"><path d="M0 2l5-2 6 2 5-2v12l-5 2-6-2-5 2z"/></svg>
  <div class="info" style="top:92px">Excepteur sint occaecat<br>cupidatat no</div>
  <svg class="info-icon" style="top:162px" width="15" height="15" viewBox="0 0 15 15" fill="#f2a43f"><path d="M3 0l3 4-2 2c1 2 3 4 5 5l2-2 4 3-2 3C6 15 0 9 0 3z"/></svg>
  <div class="info" style="top:156px">+188-888-8888</div>
  <svg class="info-icon" style="top:199px" width="16" height="12" viewBox="0 0 16 12" fill="#f2a43f"><path d="M0 0h16v12H0z"/><path d="M0 0l8 6 8-6" stroke="#2b2b2b" stroke-width="1.5" fill="none"/></svg>
  <div class="info" style="top:192px">info@companyname.com</div>

  <h4 style="left:885px">Follow Us</h4>
  <div class="social" aria-label="Social media links"><span></span><span></span><span></span><span></span><span></span></div>

  <div class="rule"></div>
  <p class="copy">Copyright ©2023 Company Name. All Rights Reserved.</p>
</footer>

</body>
</html>
```